dkfarrowplace website

I need a new homepage design for my current website at www.DKFarrowPlace.example. I want someone to look at my current website and develop a more appealing homepage... right now the colors don't blend very well and it needs a facelift

Reason: This has been extended to September 10th

```html
<!DOCTYPE html>
<html lang="en">
<head>
<meta charset="utf-8">
<title>DK Farrow — Home</title>
<link rel="stylesheet" href="https://fonts.googleapis.com/css2?family=Source+Sans+3:wght@400;600;700&display=swap">
<style>
  :root {
    --bg-center: #2c3c62;
    --bg-edge: #18203a;
    --white: #ffffff;
    --nav-text: #e6eaf3;
    --brand-blue: #27489a;
    --body-text: #444a55;
    --contact-bg: #cfe2f0;
    --contact-ink: #1d3e7a;
    --media-bar: #0f1d3f;
    --orange: #ee7a24;
    --orange-light: #f48a2e;
    --orange-dark: #d24e12;
    --divider: #34456b;
    --link: #8fc0ee;
    --footer-text: #c9cfdc;
    --press-ink: #3d4656;
  }
  * { box-sizing: border-box; margin: 0; padding: 0; }
  html, body { width: 1200px; height: 897px; overflow: hidden; }
  body {
    position: relative;
    font-family: "Source Sans 3", sans-serif;
    background: radial-gradient(ellipse at 50% 40%, var(--bg-center) 0%, #232f50 55%, var(--bg-edge) 100%);
  }
  .abs { position: absolute; }

  .brand { left: 248px; top: 52px; font-size: 30px; font-weight: 400; color: var(--white); letter-spacing: 0.5px; }
  .main-nav { right: 248px; top: 63px; display: flex; gap: 20px; list-style: none; }
  .main-nav li { font-size: 12.5px; color: var(--nav-text); }
  .main-nav li.is-active { font-weight: 700; color: var(--white); }

  .hero { left: 248px; top: 115px; width: 705px; height: 260px;
    background: linear-gradient(100deg, #e9c9a0 0%, #f0d2ad 25%, #8fc45a 40%, #5aa338 55%, #f1d6b4 70%, #5c8a35 100%); }
  .slider-arrow { top: 230px; }
  .slider-arrow.prev { left: 205px; }
  .slider-arrow.next { left: 977px; }

  .welcome { left: 248px; top: 390px; width: 464px; height: 224px; background: var(--white); padding: 32px 33px; }
  .welcome h1 { font-size: 16.5px; font-weight: 700; color: var(--brand-blue); margin-bottom: 14px; }
  .welcome p { font-size: 10.2px; line-height: 16.5px; color: var(--body-text); width: 390px; }
  .btn-learn { display: inline-block; margin-top: 13px; background: var(--brand-blue); color: var(--white);
    font-size: 9px; font-weight: 600; padding: 9px 15px; border: 1px solid #1b3478; }

  .promo-book { left: 728px; top: 390px; width: 225px; height: 104px;
    background: linear-gradient(120deg, #e4f6d9 0%, #d8f0c9 60%, #bfe6b8 100%); }
  .media-room { left: 728px; top: 510px; width: 105px; height: 105px; background: var(--media-bar); }
  .media-room .thumb { width: 105px; height: 75px; background: linear-gradient(160deg, #6b4a36 0%, #3e2a20 60%, #2a1c16 100%); }
  .media-room .label { color: var(--white); font-size: 14px; font-weight: 700; text-align: center; line-height: 29px; }
  .contact-tile { left: 848px; top: 510px; width: 105px; height: 105px; background: var(--contact-bg);
    text-align: center; color: var(--contact-ink); }
  .contact-tile svg { margin-top: 27px; }
  .contact-tile .label { font-size: 14px; font-weight: 700; margin-top: 8px; }

  .signup-band { left: 248px; top: 634px; width: 706px; height: 49px;
    background: linear-gradient(90deg, var(--orange) 0%, var(--orange-light) 50%, var(--orange) 100%); }
  .signup-band .title { left: 33px; top: 15px; font-size: 14.5px; font-weight: 700; color: var(--white); }
  .signup-band .field-label { top: 18px; font-size: 10.5px; color: var(--white); }
  .signup-band .field { top: 18px; height: 15px; background: var(--white); border: 1px solid #c9c9c9; }
  .btn-subscribe { left: 614px; top: 12px; width: 80px; height: 28px; background: var(--orange-dark);
    color: var(--white); font-size: 10.5px; text-align: center; line-height: 28px; }

  .press-row { left: 248px; top: 702px; width: 706px; display: flex; justify-content: space-between; }
  .press-tile { width: 165px; height: 62px; background: var(--white); display: flex; align-items: center; justify-content: center;
    font-size: 19px; font-weight: 600; color: var(--press-ink); }

  .footer-rule { left: 248px; top: 787px; width: 705px; height: 1px; background: var(--divider); }
  .footer-left { left: 248px; top: 812px; font-size: 10.5px; color: var(--footer-text); }
  .footer-left a { color: var(--link); text-decoration: none; }
  .footer-left a.underlined { text-decoration: underline; }
  .footer-right { right: 247px; top: 812px; font-size: 10.5px; color: var(--footer-text); }
  .footer-right strong { color: var(--white); font-weight: 600; }
</style>
</head>
<body>
  <header>
    <div class="abs brand">DK Farrow</div>
    <ul class="abs main-nav">
      <li class="is-active">Home</li>
      <li>Products</li>
      <li>About</li>
      <li>Blog</li>
      <li>Forum</li>
      <li>Media Room</li>
      <li>Success Stories</li>
    </ul>
  </header>

  <section class="abs hero" role="img" aria-label="Photo of a green smoothie with cucumber slices, lemon and kale, with the tagline: Discover secrets to a slimmer, sexier and healthier you!"></section>
  <svg class="abs slider-arrow prev" width="16" height="30" viewBox="0 0 16 30" aria-label="Previous slide"><polyline points="14,1 2,15 14,29" fill="none" stroke="#8f9ab3" stroke-width="1.3"/></svg>
  <svg class="abs slider-arrow next" width="16" height="30" viewBox="0 0 16 30" aria-label="Next slide"><polyline points="2,1 14,15 2,29" fill="none" stroke="#8f9ab3" stroke-width="1.3"/></svg>

  <section class="abs welcome">
    <h1>WELCOME TO DK FARROW</h1>
    <p>DK Farrow is a nutritionist and certified weight-loss expert, passionate relationship/life coach, and inspirational speaker. She has been featured on The Harlan Pike Morning Show, The Wendell Rooke Show, The Corin Ashby Show, and The Bram Tolliver Show. Get to know DK better through the pictures in her portfolio and at events and book signings. She shares images</p>
    <span class="btn-learn">LEARN MORE</span>
  </section>

  <div class="abs promo-book" role="img" aria-label="Banner for the book 14-Day Green Juice Reset, with a book cover"></div>

  <div class="abs media-room">
    <div class="thumb" role="img" aria-label="Video still from a media interview"></div>
    <div class="label">MEDIA ROOM</div>
  </div>

  <div class="abs contact-tile">
    <svg width="24" height="26" viewBox="0 0 24 24" aria-hidden="true"><path fill="#1d3e7a" d="M6.6 10.8c1.4 2.8 3.8 5.1 6.6 6.6l2.2-2.2c.3-.3.7-.4 1-.2 1.1.4 2.3.6 3.6.6.6 0 1 .4 1 1V20c0 .6-.4 1-1 1C10.6 21 3 13.4 3 4c0-.6.4-1 1-1h3.5c.6 0 1 .4 1 1 0 1.3.2 2.5.6 3.6.1.3 0 .7-.2 1L6.6 10.8z"/></svg>
    <div class="label">CONTACT</div>
  </div>

  <form class="abs signup-band">
    <span class="abs title">FREE REPORT :</span>
    <span class="abs field-label" style="left:144px">NAME :</span>
    <span class="abs field" style="left:181px;width:190px"></span>
    <span class="abs field-label" style="left:377px">EMAIL :</span>
    <span class="abs field" style="left:417px;width:190px"></span>
    <span class="abs btn-subscribe">SUBSCRIBE</span>
  </form>

  <div class="abs press-row">
    <div class="press-tile">Orbitwave Radio</div>
    <div class="press-tile">Radiant Daily</div>
    <div class="press-tile">HomeCircle</div>
    <div class="press-tile">Lustre</div>
  </div>

  <footer>
    <div class="abs footer-rule"></div>
    <div class="abs footer-left">Follow us on <a class="underlined" href="#">PeopleWall</a>, <a href="#">Chirper</a></div>
    <div class="abs footer-right">Copyright © 2014 <strong>DK FARROW</strong></div>
  </footer>
</body>
</html>
```